Business Cards Design for the electrical wholesaler: clean bold dynamic :)

We need a business card design that would follow our latest brand guidelines. As an electrical wholesaler we want to bring a fresh look and feel into the industry. The design should be clean bold and dynamic. It should come alive with the renewed energy of our green colour. Our grey colour should keep things balanced and complement the notion of maturity and responsibility. We employ Lato as a corporate font however are not bound by this font and we’re open to interpretation here.

Target Market(s)

Electrical contractors

Industry/Entity Type

Business

Contact Information for Business Card

Logo
Name & Surname: Olena Dovbush
Job Title: Director of Marketing
Email: helen.dovbush@mailvane.example
Cell phone: XXX.XXX.XXXX
Address: 20917 - 87 Ave. Edmonton, AB, Canada. T6K 2R8
Business Phone: 780.555.0187
Website: www.qorvil.example

Font styles to use
Other font styles liked:
• Lato

Requirements
Must have
• Logo & website
Nice to have
• Brand elements - some of them you may find in the attached Brand Guidelines (e.g. three lines on the background signifying "W")

```html
<!DOCTYPE html>
<html lang="en">
<head>
<meta charset="utf-8">
<title>qorvil business cards</title>
<link rel="stylesheet" href="https://fonts.googleapis.com/css2?family=Roboto:wght@400;500&display=swap">
<style>
  :root {
    --backdrop: #b9b9b9;
    --brand-green: #7ab622;
    --brand-green-deep: #5ea427;
    --brand-grey: #4a4c4f;
    --text-grey: #4d4d4d;
    --card-white: #f4f4f4;
    --card-white-shade: #e6e6e6;
  }
  * { box-sizing: border-box; margin: 0; padding: 0; }
  html, body { width: 1200px; height: 576px; overflow: hidden; }
  body {
    background: var(--backdrop);
    font-family: "Roboto", sans-serif;
    position: relative;
  }
  .card {
    position: absolute;
    border-radius: 11px;
    overflow: hidden;
    box-shadow: 0 2px 4px rgba(0,0,0,0.25);
  }
  .card--front {
    left: 82px; top: 138px; width: 485px; height: 294px;
    background: linear-gradient(160deg, var(--brand-green) 0%, var(--brand-green-deep) 100%);
  }
  .card--back {
    left: 602px; top: 138px; width: 482px; height: 292px;
    background: linear-gradient(160deg, var(--card-white) 40%, var(--card-white-shade) 100%);
  }
  .wordmark {
    position: absolute;
    font-family: "Roboto", sans-serif;
    font-weight: 500;
    color: var(--brand-grey);
    line-height: 1;
    letter-spacing: -0.5px;
  }
  .card--front .wordmark {
    left: 0; right: 0; top: 124px;
    text-align: center;
    font-size: 46px;
  }
  .card--back .wordmark {
    right: 20px; top: 38px;
    font-size: 40px;
  }
  .accent-tab {
    position: absolute;
    left: -24px; top: 34px;
    width: 48px; height: 48px;
    border-radius: 50%;
    background: var(--brand-green);
  }
  .holder-name {
    position: absolute;
    left: 30px; top: 45px;
    font-size: 21px;
    font-weight: 500;
    color: var(--brand-green);
  }
  .holder-title {
    position: absolute;
    left: 30px; top: 72px;
    font-size: 12.5px;
    color: var(--text-grey);
  }
  .contact {
    position: absolute;
    left: 28px; top: 193px;
    font-size: 12.5px;
    color: var(--text-grey);
    line-height: 16px;
  }
  .contact-address { margin-bottom: 6px; }
  .contact-row { display: flex; align-items: center; gap: 6px; height: 17px; }
  .contact-row + .contact-row { margin-top: 1px; }
  .contact-item { display: inline-flex; align-items: center; gap: 6px; margin-right: 6px; }
  .contact-icon { width: 12px; height: 12px; flex: none; }
</style>
</head>
<body>

  <section class="card card--front" aria-label="Card front">
    <div class="wordmark">qorvil</div>
  </section>

  <section class="card card--back" aria-label="Card back">
    <div class="accent-tab"></div>
    <div class="holder-name">Olena Dovbush</div>
    <div class="holder-title">Founder &amp; CEO</div>
    <div class="wordmark">qorvil</div>

    <div class="contact">
      <div class="contact-address">20917 - 87 Ave. Edmonton,<br>AB, Canada T6K 2R8</div>
      <div class="contact-row">
        <span class="contact-item">
          <svg class="contact-icon" viewBox="0 0 12 12" aria-hidden="true">
            <circle cx="6" cy="6" r="6" fill="var(--brand-green)"/>
            <path d="M3.5 5.2c0-.9.9-1.4 2.5-1.4s2.5.5 2.5 1.4H7.4v-.5H4.6v.5z M4.2 5.6h3.6l.4 2.6H3.8z" fill="#fff"/>
          </svg>
          +1 780-555-0187
        </span>
      </div>
      <div class="contact-row">
        <span class="contact-item">
          <svg class="contact-icon" viewBox="0 0 12 12" aria-hidden="true">
            <circle cx="6" cy="6" r="6" fill="var(--brand-green)"/>
            <rect x="3" y="4" width="6" height="4.2" fill="#fff"/>
            <path d="M3 4l3 2.3L9 4" fill="none" stroke="var(--brand-green)" stroke-width="0.7"/>
          </svg>
          hello@qorvil.example
        </span>
        <span class="contact-item">
          <svg class="contact-icon" viewBox="0 0 12 12" aria-hidden="true">
            <circle cx="6" cy="6" r="6" fill="var(--brand-green)"/>
            <circle cx="6" cy="6" r="3" fill="none" stroke="#fff" stroke-width="0.8"/>
            <path d="M3 6h6M6 3c-1.2 1.6-1.2 4.4 0 6M6 3c1.2 1.6 1.2 4.4 0 6" fill="none" stroke="#fff" stroke-width="0.6"/>
          </svg>
          qorvil.example
        </span>
      </div>
    </div>
  </section>

</body>
</html>
```